TalkWell needs a Letterhead

We need a letterhead for our company "TalkWell Consultants". Logo is attached. The company color is Turquoise. Icons for website, scan logo for website, icons for address, e-mail and phone appreciated rather than just words.

```html
<!DOCTYPE html>
<html lang="en">
<head>
<meta charset="utf-8">
<title>TalkWell Consultants Letterhead</title>
<link rel="stylesheet" href="https://fonts.googleapis.com/css2?family=Open+Sans:wght@400&display=swap">
<style>
  :root {
    --backdrop: #bdbdbd;
    --paper: #ffffff;
    --brand-blue: #1a78c2;
    --brand-green: #8cc63f;
    --tint-blue: #dde9f3;
    --tint-green: #edf5e1;
  }
  html, body {
    margin: 0;
    width: 1200px;
    height: 900px;
    overflow: hidden;
    background: var(--backdrop);
  }
  .letterhead {
    position: absolute;
    left: 302px;
    top: 96px;
    width: 558px;
    height: 724px;
    background: var(--paper);
    overflow: hidden;
  }
  .brand {
    position: absolute;
    left: 19px;
    top: 30px;
    display: flex;
    align-items: center;
    gap: 14px;
  }
  .brand-square {
    width: 44px;
    height: 44px;
    background: var(--brand-blue);
  }
  .brand-name {
    font-family: "Open Sans", sans-serif;
    font-weight: 400;
    font-size: 22px;
    color: var(--brand-blue);
    letter-spacing: 0.2px;
    line-height: 1;
  }
  .decor {
    position: absolute;
    inset: 0;
  }
</style>
</head>
<body>
  <main class="letterhead">
    <header class="brand">
      <span class="brand-square"></span>
      <span class="brand-name">TalkWell Consultants</span>
    </header>

    <svg class="decor" width="558" height="724" viewBox="0 0 558 724" aria-hidden="true">
      <circle class="corner-disc" cx="448" cy="664" r="176" fill="var(--tint-blue)" stroke="var(--tint-green)" stroke-width="2"/>
      <rect class="side-rule-green" x="517" y="170" width="4" height="310" fill="var(--tint-green)"/>
      <rect class="side-band-blue" x="524" y="170" width="17" height="310" fill="var(--tint-blue)"/>
      <rect class="foot-rule-green" x="19" y="676" width="254" height="4" fill="var(--tint-green)"/>
      <rect class="foot-band-blue" x="19" y="683" width="254" height="18" fill="var(--tint-blue)"/>
    </svg>
  </main>
</body>
</html>
```